PowerPoint template for my training workshop business

I would like to have a PowerPoint template created using my logo and palette materials created by Brivantelox. I train and facilitate workshops using PowerPoint in both corporate and public settings.

I have attached the original design elements to this request.

```html
<!DOCTYPE html>
<html lang="en">
<head>
<meta charset="utf-8">
<title>Marla Venn Coaching – Presentation Template</title>
<link href="https://fonts.googleapis.com/css2?family=League+Gothic&family=Roboto+Condensed:wght@400;500;700&display=swap" rel="stylesheet">
<style>
  :root {
    --board: #a9a9a9;
    --ink: #0b0b0b;
    --paper: #f7f7f7;
    --gold: #f3b61f;
    --amber: #f09a1a;
    --white: #ffffff;
    --photo-light: #d9d9d9;
    --photo-dark: #5a5a5a;
    --text: #1a1a1a;
  }
  * { box-sizing: border-box; margin: 0; padding: 0; }
  html, body { width: 1200px; height: 863px; overflow: hidden; background: var(--board); }
  body { position: relative; font-family: "Roboto Condensed", Arial, sans-serif; color: var(--text); }

  .slide { position: absolute; width: 510px; height: 287px; overflow: hidden; }
  .slide--cover   { left: 61px;  top: 97px;  background: var(--ink); }
  .slide--content { left: 620px; top: 97px;  background: var(--paper); }
  .slide--contact { left: 61px;  top: 476px; background: var(--paper); }
  .slide--closing { left: 620px; top: 476px; background: var(--ink); }

  .brand { position: absolute; display: flex; align-items: center; gap: 6px;
    font-family: "Roboto Condensed", Arial, sans-serif; font-weight: 700;
    color: var(--gold); text-transform: uppercase; white-space: nowrap; }
  .brand__dot { border-radius: 50%; background: var(--gold); flex: none; }

  .label { position: absolute; background: var(--gold); color: var(--ink);
    font-family: "League Gothic", "Arial Narrow", sans-serif; font-weight: 400; line-height: 1;
    display: flex; align-items: center; white-space: nowrap;
    box-shadow: 6px 6px 0 var(--white); }

  /* Cover */
  .cover__photo { position: absolute; inset: 0;
    clip-path: polygon(39% 0, 100% 0, 100% 100%, 52.7% 100%);
    background: linear-gradient(120deg, var(--photo-dark), var(--photo-light) 55%, #9a9a9a); }
  .cover__brand { left: 16px; top: 32px; font-size: 16px; }
  .cover__brand .brand__dot { width: 42px; height: 42px; }
  .cover__year { position: absolute; left: 26px; top: 105px; font-family: "League Gothic", "Arial Narrow", sans-serif;
    font-size: 64px; line-height: 1; color: var(--gold); }
  .cover__title { left: 16px; top: 158px; height: 61px; font-size: 68px; padding: 4px 18px 0 10px; }
  .cover__web { position: absolute; left: 16px; top: 253px; font-size: 9px; letter-spacing: 3.6px; color: var(--white); }

  /* Content */
  .content__rail { position: absolute; left: 0; top: 0; width: 78px; height: 100%; background: var(--ink); }
  .content__label { left: 34px; top: 13px; height: 34px; font-size: 38px; padding: 3px 12px 0 9px; }
  .content__brand { right: 9px; top: 11px; font-size: 10px; }
  .content__brand .brand__dot { width: 22px; height: 22px; }
  .content__heading { position: absolute; left: 85px; top: 58px; font-size: 10px; font-weight: 700; color: var(--amber);
    border-bottom: 1px solid var(--amber); line-height: 1.2; }
  .content__body { position: absolute; left: 85px; top: 74px; width: 417px; font-size: 6.6px; line-height: 1.36; text-align: justify; }
  .frame { position: absolute; background: var(--ink); color: var(--white); font-weight: 700;
    display: flex; align-items: center; justify-content: center; }
  .frame--main { left: 85px; top: 143px; width: 189px; height: 126px; font-size: 27px; }
  .frame--top  { left: 282px; top: 143px; width: 62px; height: 44px; font-size: 9.5px; }
  .frame--side { left: 282px; top: 192px; width: 98px; height: 65px; font-size: 14px; }
  .page-num { position: absolute; left: 478px; top: 248px; width: 20px; height: 20px; border-radius: 50%;
    background: var(--gold); border: 1.5px solid var(--ink); font-size: 11px; font-weight: 700;
    display: flex; align-items: center; justify-content: center; }

  /* Contact */
  .contact__backdrop { position: absolute; inset: 0; background: linear-gradient(90deg, #e9e9e9, var(--paper) 70%); }
  .contact__panel { position: absolute; inset: 0; background: var(--ink);
    clip-path: polygon(0 0, 29.6% 0, 43.2% 100%, 0 100%); }
  .contact__label { left: 30px; top: 13px; height: 50px; font-size: 52px; padding: 5px 20px 0 15px; }
  .contact__brand { right: 9px; top: 13px; font-size: 10px; }
  .contact__brand .brand__dot { width: 22px; height: 22px; }
  .contact__name { position: absolute; left: 188px; top: 92px; font-size: 25px; font-weight: 500; color: var(--ink); white-space: nowrap; }
  .contact__row { position: absolute; display: flex; align-items: center; font-size: 11px; color: var(--ink); white-space: nowrap; }
  .contact__icon { width: 16px; height: 16px; flex: none; }
  .row--addr  { left: 158px; top: 140px; gap: 19px; }
  .row--phone { left: 165px; top: 173px; gap: 22px; }
  .row--mail  { left: 174px; top: 204px; gap: 20px; }
  .row--web   { left: 184px; top: 239px; gap: 19px; }

  /* Closing */
  .closing__brand { left: 50%; top: 50%; transform: translate(-50%, -50%); font-size: 30px; gap: 14px; }
  .closing__brand .brand__dot { width: 72px; height: 72px; }
</style>
</head>
<body>

  <section class="slide slide--cover">
    <div class="cover__photo" role="img" aria-label="Black and white photo of workshop participants writing at a table"></div>
    <div class="brand cover__brand"><span class="brand__dot"></span>Marla Venn Coaching</div>
    <div class="cover__year">2020</div>
    <h1 class="label cover__title">PRESENTATION</h1>
    <p class="cover__web">WWW.MARLAVENNCOACHING.COM</p>
  </section>

  <section class="slide slide--content">
    <div class="content__rail"></div>
    <h2 class="label content__label">SLIDE</h2>
    <div class="brand content__brand"><span class="brand__dot"></span>Marla Venn Coaching</div>
    <h3 class="content__heading">LOREM IPSUM</h3>
    <p class="content__body">Lorem ipsum dolor sit amet, consectetur adipiscing elit, sed do eiusmod tempor incididunt ut labore et dolore magna aliqua. Ut enim ad minim veniam, quis nostrud exercitation ullamco laboris nisi ut aliquip ex ea commodo consequat. Duis aute irure dolor in reprehenderit in voluptate velit esse cillum dolore eu fugiat nulla pariatur. Excepteur sint occaecat cupidatat non proident, sunt in culpa qui officia deserunt mollit anim id est laborum.Lorem ipsum dolor sit amet, consectetur adipiscing elit, sed do eiusmod tempor incididunt ut labore et dolore magna aliqua. Ut enim ad minim veniam, quis nostrud exercitation ullamco laboris nisi ut aliquip ex ea commodo consequat. Duis aute irure dolor in reprehenderit in voluptate velit esse cillum dolore eu fugiat nulla pariatur. Excepteur sint occaecat cupidatat non proident, sunt in culpa qui officia deserunt mollit anim id est laborum.</p>
    <div class="frame frame--main">IMAGE</div>
    <div class="frame frame--top">IMAGE</div>
    <div class="frame frame--side">IMAGE</div>
    <div class="page-num">1</div>
  </section>

  <section class="slide slide--contact">
    <div class="contact__backdrop" role="img" aria-label="Faint washed-out photo of a workshop group"></div>
    <div class="contact__panel"></div>
    <h2 class="label contact__label">CONTACT SLIDE</h2>
    <div class="brand contact__brand"><span class="brand__dot"></span>Marla Venn Coaching</div>
    <h3 class="contact__name">MARLA VENN COACHING</h3>
    <div class="contact__row row--addr">
      <svg class="contact__icon" viewBox="0 0 16 16" fill="none" stroke="#fff" stroke-width="1.2"><circle cx="8" cy="8" r="7.3"/><path d="M8 12.5s-3-3.2-3-5.3a3 3 0 0 1 6 0c0 2.1-3 5.3-3 5.3z"/><circle cx="8" cy="7.2" r="1"/></svg>
      <span>LOREM IPSUM DOLOR SIT AMET, CONSECTETUR ADIPISCING ELIT</span>
    </div>
    <div class="contact__row row--phone">
      <svg class="contact__icon" viewBox="0 0 16 16" fill="none" stroke="#fff" stroke-width="1.2"><circle cx="8" cy="8" r="7.3"/><path d="M5.2 4.3l1.4-.3.8 2-1 .8c.5 1.1 1.4 2 2.5 2.5l.8-1 2 .8-.3 1.4c-3.5.3-6.5-2.7-6.2-6.2z" fill="#fff"/></svg>
      <span>12345 - 54321</span>
    </div>
    <div class="contact__row row--mail">
      <svg class="contact__icon" viewBox="0 0 16 16" fill="none" stroke="#fff" stroke-width="1.2"><circle cx="8" cy="8" r="7.3"/><rect x="4.3" y="5.3" width="7.4" height="5.4" rx=".6" fill="#fff" stroke="none"/><path d="M4.6 5.8 8 8.3l3.4-2.5" stroke="#0b0b0b"/></svg>
      <span>MARLAVENNCOACHING@MAIL.COM</span>
    </div>
    <div class="contact__row row--web">
      <svg class="contact__icon" viewBox="0 0 16 16" fill="none" stroke="#0b0b0b" stroke-width="1"><circle cx="8" cy="8" r="7.3"/><circle cx="8" cy="8" r="4.3"/><path d="M3.7 8h8.6M8 3.7v8.6M5.6 4.8c1.4 2 1.4 4.4 0 6.4M10.4 4.8c-1.4 2-1.4 4.4 0 6.4"/></svg>
      <span>WWW.MARLAVENNCOACHING.COM</span>
    </div>
  </section>

  <section class="slide slide--closing">
    <div class="brand closing__brand"><span class="brand__dot"></span>Marla Venn Coaching</div>
  </section>

</body>
</html>
```